Las Vegas Tour guide needs website of future for physical and selfguided assets

Strip Lantern is the parent site to my Las Vegas tour operation. Within this is a physical walking tour called Shadows and the Syndicate, the site traffic driver where I tell history with a paranormal twist. The legacy site can be seen at spectralalleywalks.example.
The Strip Lantern app has self guided tours called Desert Hops Trail/Shadows and The Syndicate Revisited/Lanternway Lane Walk. Kirvo is a 3rd party tour company I have partnered with to sale self-guided tours with a scavenger hunt theme.
I like black and pink and pistachio green colors however am flexible in theme. Colors should follow Vegas 50-60s aesthetics. The “Greetings From Neon Gulch Marker” should not be considered as design inspiration. 95% of traffic is on mobile. Final design should be easy to understand guided versus self-guided option. Show cross promotion links for digital assets/physical tour. Kirvo content tbd by end of week 9 Aug 2021
sites i like
nationalspookstrolls.example
marshesandspirits.example
oldharborphantomwalks.example
Updates

Needs a book now at top, or floating like brelvatours. Less busy and stay away from using photos. I have included more websites for inspiration. I would like a mashup of the two sites extraperceptsite and brelvatours. I am unsure what some of your designs would look like on a mobile screen. Please screenshot that. https://extraperceptsite.example/ https://www.brelvatours.example/ https://qp7lz.example/ https://metrowraiths.example/ https://leadhoundwalks.example/tours/new-york-city/phantoms-of-ashbury-quarter/

Family member hospitalized need extra time to review

Target Market(s)

Tourist 25+

Industry/Entity Type

Travel. Tour guide.

Coding

Coded - Design and coding required

Number of Pages Required

5+ page

Font styles to use
Serif

Colors
00AB8E
00BBA5
67D7C9
C6EFE9
E9F9F6
59FF00
82FF00
B8FF75
E3FFCB
F4FFEA
EB3D1F
EC4F4E
F09395
F8D3D4
FCEDEE
E54698
E96AAD
F1A4CE
F9D9EA
FCEFF6

Requirements
Must have
• Cross promotion between physical tour and digital
Nice to have
• sliver button like ads as breaks between tour info
Should not have
• "Greetings from Neon Gulch Marker". no photos. no animation.

```html
<!DOCTYPE html>
<html lang="en">
<head>
<meta charset="utf-8">
<title>Shadows and the Syndicate Las Vegas Walking Tour</title>
<link href="https://fonts.googleapis.com/css2?family=Montserrat:ital,wght@0,400;0,500;0,600;0,700;1,700;1,900&display=swap" rel="stylesheet">
<style>
  :root {
    --ink: #050505;
    --panel: #121212;
    --white: #ffffff;
    --muted: #bdbdbd;
    --lime: #5fe000;
    --lime-bright: #82ff00;
    --forest: #123008;
    --silver-hi: #f4f4f4;
    --silver-lo: #9a9a9a;
  }
  * { box-sizing: border-box; margin: 0; padding: 0; }
  html, body { width: 897px; height: 1200px; overflow: hidden; background: var(--ink); }
  body { font-family: "Montserrat", sans-serif; color: var(--white); position: relative; }

  .page-backdrop {
    position: absolute; inset: 0;
    background:
      radial-gradient(ellipse 40% 18% at 12% 52%, rgba(180,180,180,.28), transparent 70%),
      radial-gradient(ellipse 38% 16% at 90% 62%, rgba(170,170,170,.22), transparent 70%),
      radial-gradient(ellipse 50% 20% at 50% 88%, rgba(120,120,120,.18), transparent 70%),
      linear-gradient(180deg, #0a0a0a 0%, #050505 100%);
  }

  .hero {
    position: absolute; left: 0; top: 0; width: 897px; height: 480px;
    background:
      linear-gradient(180deg, rgba(0,0,0,.55) 0%, rgba(0,0,0,.15) 45%, rgba(5,5,5,1) 100%),
      radial-gradient(ellipse 30% 45% at 82% 30%, #7a5a2a, transparent 70%),
      radial-gradient(ellipse 25% 40% at 62% 45%, #4a3a22, transparent 70%),
      radial-gradient(ellipse 40% 30% at 45% 75%, #2c3a4a, transparent 70%),
      linear-gradient(180deg, #14100c, #1b1814);
  }

  .brand { position: absolute; left: 80px; top: 60px; display: flex; align-items: center; gap: 10px; }
  .brand-mark { width: 34px; height: 34px; border-radius: 50%; background: var(--lime); }
  .brand-name { font-weight: 700; font-size: 16px; color: var(--white); letter-spacing: .5px; }

  .site-nav { position: absolute; right: 0; top: 58px; text-align: right; }
  .site-nav ul { list-style: none; }
  .site-nav li { font-size: 9.5px; font-weight: 500; line-height: 17px; padding-right: 118px; }
  .site-nav li.is-current { color: var(--lime); font-weight: 600; position: relative; }
  .site-nav li.is-current::after {
    content: ""; position: absolute; right: 0; top: 9px; width: 108px; height: 1px; background: var(--lime);
  }

  .hero-title { position: absolute; left: 0; right: 0; top: 200px; text-align: center; transform: rotate(-4deg); }
  .hero-kicker { font-style: italic; font-weight: 700; font-size: 21px; color: var(--lime); letter-spacing: .5px; margin-left: -20px; }
  .hero-city { font-style: italic; font-weight: 900; font-size: 78px; line-height: 1; letter-spacing: 1px; text-shadow: 0 4px 10px rgba(0,0,0,.6); }
  .hero-sub { font-style: italic; font-weight: 700; font-size: 30px; color: var(--lime); letter-spacing: 1px; margin-left: -10px; }

  .silver-button {
    position: absolute; left: 50%; top: 400px; transform: translateX(-50%);
    width: 136px; height: 30px; display: flex; align-items: center; justify-content: center;
    background: linear-gradient(180deg, var(--silver-hi) 0%, #d0d0d0 55%, var(--silver-lo) 100%);
    border: 1px solid #777; border-radius: 2px;
    font-size: 9.5px; font-weight: 700; color: #111; letter-spacing: .6px; text-decoration: none;
    box-shadow: 0 2px 6px rgba(0,0,0,.6);
  }

  .connector { position: absolute; left: 448px; width: 1.5px; background: var(--lime); }
  .connector-top { top: 452px; height: 40px; }
  .connector-bottom { top: 822px; height: 32px; }

  .tour-card {
    position: absolute; left: 150px; top: 492px; width: 598px; height: 330px;
    background: var(--panel); padding: 40px 72px 0 72px;
  }
  .tour-card h2 { font-size: 15px; font-weight: 600; line-height: 22px; letter-spacing: .4px; text-transform: uppercase; }
  .tour-card h3 { font-size: 14px; font-weight: 600; letter-spacing: .4px; margin-top: 26px; margin-bottom: 12px; }
  .tour-list { list-style: none; margin-top: 16px; }
  .tour-list li { font-size: 9px; color: var(--muted); line-height: 17px; padding-left: 14px; position: relative; }
  .tour-list li::before { content: "-"; position: absolute; left: 2px; }
  .tour-list.details { margin-top: 0; }

  .app-promo { position: absolute; left: 0; right: 0; top: 880px; text-align: center; }
  .app-promo h2 { font-size: 14px; font-weight: 700; line-height: 22px; letter-spacing: .8px; text-transform: uppercase; }
  .store-links { display: flex; justify-content: center; gap: 12px; margin-top: 30px; }
  .store-link {
    display: flex; align-items: center; gap: 8px; height: 34px; padding: 0 16px 0 8px;
    border-radius: 17px; background: #1c1c1c; color: var(--white); text-decoration: none;
    font-size: 10px; font-weight: 600;
  }
  .store-dot { width: 20px; height: 20px; border-radius: 50%; background: var(--white); }

  .site-footer {
    position: absolute; left: 22px; right: 22px; top: 1048px; height: 152px;
    background: linear-gradient(180deg, var(--forest), #0c1f06);
    text-align: center; padding-top: 28px;
  }
  .social-links { display: flex; justify-content: center; gap: 14px; }
  .social-dot { width: 30px; height: 30px; border-radius: 50%; background: var(--lime-bright); display: block; }
  .footer-contact { font-size: 15px; margin-top: 20px; }
  .footer-legal { font-size: 9px; color: var(--muted); margin-top: 12px; }
</style>
</head>
<body>
  <div class="page-backdrop" role="img" aria-label="Dark misty background with drifting smoke and forest silhouettes"></div>

  <header class="hero" role="img" aria-label="Night view of the Las Vegas Strip with lit hotel towers">
  </header>

  <a class="brand" href="#">
    <span class="brand-mark"></span>
    <span class="brand-name">Lanternway Lane Walk</span>
  </a>

  <nav class="site-nav">
    <ul>
      <li class="is-current">Shadows and The Syndicate Las Vegas</li>
      <li>Strip Lantern App</li>
      <li>Desert Hops Trail</li>
      <li>Contact Us</li>
      <li>Redeem Voucher</li>
      <li>Cancellation Policy</li>
      <li>Privacy Policy</li>
    </ul>
  </nav>

  <div class="hero-title">
    <p class="hero-kicker">SHADOWS AND THE SYNDICATE</p>
    <h1 class="hero-city">LAS VEGAS</h1>
    <p class="hero-sub">WALKING TOURS</p>
  </div>

  <a class="silver-button" href="#">BOOK NOW</a>

  <span class="connector connector-top"></span>

  <section class="tour-card">
    <h2>Explore downtown Las Vegas and hear the history of Lanternway Lane with a paranormal twist!</h2>
    <ul class="tour-list">
      <li>Visit 3 haunted Las Vegas properties and hear the real stories that made them as they are</li>
      <li>Highlights include the ghosts of syndicate bodyguards and stories from the Motel of Death!</li>
      <li>Explore historic Downtown Las Vegas with an experienced guide on Lanternway Lane</li>
    </ul>
    <h3>DETAILS</h3>
    <ul class="tour-list details">
      <li>45 Minute walking tour</li>
      <li>Tour route less than one mile on accessible roads and sidewalks</li>
      <li>Rain or shine we almost always operate!</li>
    </ul>
  </section>

  <span class="connector connector-bottom"></span>

  <section class="app-promo">
    <h2>Shadows and the Syndicate Las Vegas Revisited<br>self guided tour also on Strip Lantern<br>app!</h2>
    <div class="store-links">
      <a class="store-link" href="#"><span class="store-dot"></span>Orchard Store</a>
      <a class="store-link" href="#"><span class="store-dot"></span>Playfield Market</a>
    </div>
  </section>

  <footer class="site-footer">
    <div class="social-links">
      <a class="social-dot" href="#" aria-label="Reviews"></a>
      <a class="social-dot" href="#" aria-label="Photos"></a>
    </div>
    <p class="footer-contact">Questions? Email us at hello@lanternwaylanewalk.example</p>
    <p class="footer-legal">Copyright © 2019 Strideandspeak LLC All Rights Reserved.</p>
  </footer>
</body>
</html>
```